Zielgruppe
wir sind eine Sicherheitsunternehmen und suchen ein ausgefallenes Design um alle Privathaushalte sowohl auch kleine und große Firmen zu beindrucken.
Aufgabenstellung
Die Firma möchte das erste Sicherheitsunternehmen sein was absolut Nachhaltig, ökologisch und umweltfreundlich arbeitet. Die Natur, der Klimawechsel steht im absoluten Vordergrund. Wir möchten zeigen das man auch als Dienstleister im Sicheheitsbereich im Einklang mit der Umwelt sein kann. und mit diesem Konzept möchten wir an die Bevölkerung rantreten. Das Motto: mit uns als Partner werden Fremdfirmen mehr Kunden gewinnen, da wir umweltbewusst und mit den uns verfügbaren Ressourcen sehr ökologisch und grün sind. Das Design sollte bitte nicht in schrillen Farben dargestellt werden. Das Logo und unsere Grundfarben sind Schwarz/ Antrazith/ Weiss/Creme und Naturrholzfarben.

```html
<!DOCTYPE html>
<html lang="de">
<head>
<meta charset="utf-8">
<title>Lumen Sicherheit – Broschüre</title>
<link href="https://fonts.googleapis.com/css2?family=Roboto:wght@400;700;900&display=swap" rel="stylesheet">
<style>
  :root {
    --canvas: #f4f4f4;
    --panel: #e8e8e8;
    --paper: #ffffff;
    --gold: #b8955f;
    --tan: #c9ae86;
    --cream: #ece2c4;
    --anthracite: #474747;
    --grey-text: #6d6d6d;
    --title-muted: #8f8a80;
  }
  * { margin: 0; padding: 0; box-sizing: border-box; }
  html, body { width: 764px; height: 1200px; overflow: hidden; }
  body {
    background: var(--canvas);
    font-family: "Roboto", Arial, sans-serif;
    position: relative;
  }
  .panel {
    position: absolute;
    left: 189px;
    width: 387px;
    height: 247px;
    background: var(--panel);
    box-shadow: 0 1px 2px rgba(0,0,0,.12);
    display: flex;
    align-items: center;
    justify-content: center;
  }
  .panel--cover { top: 74px; }
  .panel--intro { top: 353px; }
  .panel--services { top: 632px; }
  .panel--outside { top: 911px; }

  .spread { display: flex; box-shadow: 0 3px 8px rgba(0,0,0,.18); }
  .page {
    position: relative;
    width: 160px;
    height: 160px;
    background: var(--paper);
    overflow: hidden;
  }
  .page--solo { box-shadow: 0 3px 8px rgba(0,0,0,.18); }
  .page svg.page-art { position: absolute; inset: 0; width: 100%; height: 100%; }
  .page > *:not(svg) { position: absolute; }

  /* cover */
  .cover-title {
    left: 9px; top: 20px;
    font-weight: 900; font-size: 12.5px; line-height: 1.05;
    text-transform: uppercase;
  }
  .cover-title .muted { color: var(--title-muted); display: block; }
  .cover-title .strong { color: #fff; display: block; }
  .wordmark {
    display: flex; align-items: center; gap: 3px;
    font-weight: 700; font-size: 3.8px; letter-spacing: .3px;
    color: var(--anthracite); text-transform: uppercase; white-space: nowrap;
  }
  .wordmark .mark { width: 6px; height: 6px; background: var(--anthracite); flex: none; }
  .cover-brand { left: 22px; top: 124px; }
  .cover-url {
    left: 98px; top: 132px;
    font-weight: 700; font-size: 5px; letter-spacing: .5px; color: var(--anthracite);
    white-space: nowrap;
  }

  /* intro spread */
  .lock-icon { left: 20px; top: 82px; width: 9px; height: 10px; }
  .intro-claim {
    left: 14px; top: 96px; width: 64px;
    color: #fff; font-weight: 700; font-size: 5px; line-height: 1.1;
  }
  .section-title {
    font-weight: 900; color: var(--anthracite); text-transform: uppercase; line-height: 1.05;
  }
  .about-title { left: 40px; top: 30px; font-size: 9px; }
  .about-rule { left: 40px; top: 44px; width: 90px; height: 0.6px; background: #cfcfcf; }
  .body-copy { font-size: 3.6px; line-height: 1.45; color: var(--grey-text); }
  .about-copy { left: 36px; top: 54px; width: 100px; }

  /* services spread */
  .objekt-title { left: 22px; top: 18px; font-size: 11px; }
  .list { list-style: none; font-size: 3.6px; line-height: 1.45; color: var(--grey-text); }
  .objekt-list { left: 44px; top: 133px; }
  .objekt-copy { left: 94px; top: 131px; width: 58px; }
  .werk-title { left: 82px; top: 12px; font-size: 7px; }
  .werk-copy { left: 82px; top: 24px; width: 70px; }
  .event-title { left: 10px; top: 96px; font-size: 7px; }
  .event-list { left: 10px; top: 116px; }

  /* back cover */
  .back-brand { left: 30px; top: 18px; }
  .contact {
    left: 30px; top: 32px; width: 110px;
    display: grid; grid-template-columns: 16px auto;
    font-size: 3.8px; line-height: 1.5; color: var(--anthracite);
  }
  .contact dd { font-weight: 700; white-space: nowrap; }
</style>
</head>
<body>

<svg width="0" height="0" style="position:absolute" aria-hidden="true">
  <defs>
    <linearGradient id="goldGrad" x1="0" y1="0" x2="1" y2="1">
      <stop offset="0" stop-color="#d2bb93"/><stop offset="1" stop-color="#a8844f"/>
    </linearGradient>
    <linearGradient id="greyPhoto" x1="0" y1="0" x2="1" y2="1">
      <stop offset="0" stop-color="#c4c4c4"/><stop offset=".5" stop-color="#8a8a8a"/><stop offset="1" stop-color="#4a4a4a"/>
    </linearGradient>
    <linearGradient id="chainGrad" x1="0" y1="0" x2="1" y2="1">
      <stop offset="0" stop-color="#c9b49a"/><stop offset="1" stop-color="#8a6a48"/>
    </linearGradient>
    <linearGradient id="lobbyGrad" x1="0" y1="0" x2="1" y2="1">
      <stop offset="0" stop-color="#d8c2a0"/><stop offset=".5" stop-color="#b57a3e"/><stop offset="1" stop-color="#8c6a48"/>
    </linearGradient>
    <linearGradient id="buildingGrad" x1="0" y1="0" x2="0" y2="1">
      <stop offset="0" stop-color="#c99f80"/><stop offset="1" stop-color="#7e9bb0"/>
    </linearGradient>
    <linearGradient id="eventGrad" x1="0" y1="0" x2="1" y2="1">
      <stop offset="0" stop-color="#ece4e0"/><stop offset="1" stop-color="#5e5560"/>
    </linearGradient>
    <linearGradient id="backPhoto" x1="0" y1="0" x2="1" y2="1">
      <stop offset="0" stop-color="#8a7d70"/><stop offset="1" stop-color="#5f554c"/>
    </linearGradient>
  </defs>
</svg>

<!-- Front cover -->
<section class="panel panel--cover">
  <article class="page page--solo">
    <svg class="page-art" viewBox="0 0 100 100" preserveAspectRatio="none">
      <polygon points="58,0 100,0 100,74 52,74" fill="url(#greyPhoto)" role="img" aria-label="Schwarzweißfoto: Hand übergibt eine Schlüsselkarte"/>
      <polygon points="0,0 58,0 52,74 0,46" fill="url(#goldGrad)"/>
      <polygon points="0,88 52,78 52,74 100,74 100,100 0,100" fill="var(--cream)"/>
    </svg>
    <h1 class="cover-title"><span class="muted">Für Ihre</span><span class="strong">Sicherheit</span></h1>
    <div class="wordmark cover-brand"><span class="mark"></span>Lumen Sicherheit</div>
    <p class="cover-url">www.lumen-schutz.de</p>
  </article>
</section>

<!-- Inside cover + Über uns -->
<section class="panel panel--intro">
  <div class="spread">
    <article class="page">
      <svg class="page-art" viewBox="0 0 100 100" preserveAspectRatio="none">
        <polygon points="0,0 36,0 62,82 0,82" fill="url(#goldGrad)"/>
        <path d="M36,0 L100,0 Q98,40 62,88 Z" fill="url(#chainGrad)" role="img" aria-label="Foto: Kette mit Vorhängeschloss"/>
      </svg>
      <svg class="lock-icon" viewBox="0 0 10 11" aria-hidden="true">
        <path d="M2.5,5 V3.2 a2.5,2.5 0 0 1 5,0 V5" fill="none" stroke="#fff" stroke-width="1"/>
        <rect x="1" y="5" width="8" height="5.5" rx="0.6" fill="none" stroke="#fff" stroke-width="1"/>
      </svg>
      <p class="intro-claim">Lorem ipsum dolor sit amet dolor sit lorem amet ipsum</p>
    </article>
    <article class="page">
      <h2 class="section-title about-title">Über uns</h2>
      <div class="about-rule"></div>
      <p class="body-copy about-copy">Sicherheit bedeutet für uns Vertrauen. Wir schützen Menschen, Gebäude und Werte mit erfahrenen Teams, klaren Abläufen und modernen Mitteln. Dabei achten wir auf Ressourcen, kurze Wege und einen respektvollen Umgang mit der Umwelt. Unsere Kunden erhalten Lösungen, die zuverlässig, ruhig und nachhaltig wirken.</p>
    </article>
  </div>
</section>

<!-- Leistungen -->
<section class="panel panel--services">
  <div class="spread">
    <article class="page">
      <svg class="page-art" viewBox="0 0 100 100" preserveAspectRatio="none">
        <polygon points="0,30 100,22 100,70 24,82 0,82" fill="url(#lobbyGrad)" role="img" aria-label="Foto: Eingangshalle mit Holzwand und warmem Licht"/>
        <polygon points="0,30 0,82 22,82" fill="var(--tan)" opacity="0.8"/>
      </svg>
      <h2 class="section-title objekt-title">Objektschutz</h2>
      <ul class="list objekt-list">
        <li>Zutrittskontrolle</li><li>Empfangsdienst</li><li>Streifengänge</li><li>Alarmverfolgung</li><li>Schlüsselverwaltung</li>
      </ul>
      <p class="body-copy objekt-copy">Wir sichern Büros, Praxen und Wohnanlagen rund um die Uhr mit geschultem Personal.</p>
    </article>
    <article class="page">
      <svg class="page-art" viewBox="0 0 100 100" preserveAspectRatio="none">
        <polygon points="0,0 48,0 48,56 0,56" fill="url(#buildingGrad)" role="img" aria-label="Foto: Industriegebäude mit Sheddach"/>
        <polygon points="0,0 18,0 0,20" fill="var(--tan)" opacity="0.7"/>
        <polygon points="54,34 100,30 100,86 62,86" fill="url(#eventGrad)" role="img" aria-label="Foto: Publikum bei einem Konzert im Scheinwerferlicht"/>
      </svg>
      <h2 class="section-title werk-title">Werkschutz</h2>
      <p class="body-copy werk-copy">Schutz von Betrieben, Lagern und Produktionsflächen mit festen Teams.</p>
      <h2 class="section-title event-title">Veranstaltungs-<br>schutz</h2>
      <ul class="list event-list">
        <li>Konzerte</li><li>Messen</li><li>Stadtfeste</li><li>Firmenfeiern</li><li>Sportveranstaltungen</li>
      </ul>
    </article>
  </div>
</section>

<!-- Rückseite + Titel -->
<section class="panel panel--outside">
  <div class="spread">
    <article class="page">
      <svg class="page-art" viewBox="0 0 100 100" preserveAspectRatio="none">
        <polygon points="62,0 100,0 100,26" fill="url(#goldGrad)"/>
        <polygon points="0,50 100,66 100,100 0,100" fill="url(#backPhoto)" role="img" aria-label="Foto: Kette mit Vorhängeschloss in warmem Grauton"/>
        <polygon points="0,50 36,56 0,68" fill="var(--tan)" opacity="0.8"/>
      </svg>
      <div class="wordmark back-brand"><span class="mark"></span>Lumen Sicherheit</div>
      <dl class="contact">
        <dt>Tel.</dt><dd>0176 00 12 3456</dd>
        <dt>E-Mail</dt><dd>info@lumen-schutz.de</dd>
        <dt>Web</dt><dd>www.lumen-schutz.de</dd>
      </dl>
    </article>
    <article class="page">
      <svg class="page-art" viewBox="0 0 100 100" preserveAspectRatio="none">
        <polygon points="58,0 100,0 100,74 52,74" fill="url(#greyPhoto)" role="img" aria-label="Schwarzweißfoto: Hand übergibt eine Schlüsselkarte"/>
        <polygon points="0,0 58,0 52,74 0,46" fill="url(#goldGrad)"/>
        <polygon points="0,88 52,78 52,74 100,74 100,100 0,100" fill="var(--cream)"/>
      </svg>
      <h1 class="cover-title"><span class="muted">Für Ihre</span><span class="strong">Sicherheit</span></h1>
      <div class="wordmark cover-brand"><span class="mark"></span>Lumen Sicherheit</div>
      <p class="cover-url">www.lumen-schutz.de</p>
    </article>
  </div>
</section>

</body>
</html>
```